Business Card Design Project

We have a logo design and are now looking for a business card design. We supply pre-construction services to the Wireless Telecommunication Industry in the development of cell phone tower and other antenna supporting infrastructure e.g. buildings. The types of services include Real Estate Leasing, Zoning & Permitting,Surveying and A&E work. I am looking for a card that includes the logo we have selected along with the full company name. Company colors are Blue and Silver. I want something professional and that "pops". Use your imagination with the four sided star portion of the logo - it can be stretched such that it occupies a large portion of the card or kept simple the way it is. I am interested in seeing the design on a white, silver, navy, black or charcoal background or any other color you think works well with the logo. Apart from the logo that includes LNI we also need to see the full company name on the card - Lanternway Networks, Inc. The design must also show a persons name, title, address, (2) phone numbers, e-mail address and web address www.lni-sample.co

Target Market(s)

Cell phone carriers e.g. Coravent Mobile, QB&R, K-Cellix, Dunmo etc.

Industry/Entity Type

Cell Phone

Requirements
Must have
• Logo and
Lanternway Networks, Inc.

```html
<!DOCTYPE html>
<html lang="en">
<head>
<meta charset="utf-8">
<title>Lanternway Networks, Inc. — Business Card</title>
<link rel="stylesheet" href="https://fonts.googleapis.com/css2?family=Open+Sans:wght@400;600&family=Roboto+Condensed:wght@700&display=swap">
<style>
  :root {
    --bg: #6b6b6d;
    --card-dark: #231f20;
    --card-light: #f7f7f5;
    --brand-blue: #2ea3e3;
    --deep-blue: #1d5f9c;
    --silver: #c9ccd1;
    --ink: #111111;
    --navy-ink: #16355c;
    --muted-curve: #dfe3e7;
  }
  * { box-sizing: border-box; margin: 0; padding: 0; }
  html, body {
    width: 1200px; height: 780px; overflow: hidden;
    background: var(--bg);
  }
  .canvas {
    width: 1200px; height: 780px;
    display: flex; align-items: center; justify-content: center; gap: 60px;
  }
  .card {
    position: relative;
    width: 520px; height: 297px;
    overflow: hidden;
    box-shadow: 0 10px 24px rgba(0,0,0,0.35);
  }

  /* Front */
  .card-front { background: var(--card-dark); }
  .front-mark {
    position: absolute; left: 70px; top: 50%;
    transform: translateY(-50%);
    display: flex; align-items: center; gap: 26px;
  }
  .front-mark .dot {
    width: 96px; height: 96px; border-radius: 50%;
    background: var(--brand-blue);
  }
  .front-mark .wordmark {
    font-family: "Roboto Condensed", "Arial Narrow", sans-serif;
    font-weight: 700; font-size: 120px; line-height: 1;
    letter-spacing: 4px;
    color: var(--silver);
  }

  /* Back */
  .card-back { background: var(--card-light); }
  .company-name {
    position: absolute; left: 30px; top: 34px;
    font-family: "Roboto Condensed", "Arial Narrow", sans-serif;
    font-weight: 700; font-size: 21px; color: var(--ink);
  }
  .person {
    position: absolute; left: 78px; top: 92px; width: 210px;
  }
  .person-name {
    font-family: "Roboto Condensed", "Arial Narrow", sans-serif;
    font-weight: 700; font-size: 20px; color: var(--navy-ink);
    padding-bottom: 4px;
    border-bottom: 2px solid var(--deep-blue);
  }
  .person-title {
    margin-top: 3px; padding-left: 72px;
    font-family: "Roboto Condensed", "Arial Narrow", sans-serif;
    font-weight: 700; font-size: 14px; color: var(--ink);
  }
  .contact {
    position: absolute; left: 330px; top: 104px;
    list-style: none;
    font-family: "Open Sans", Arial, sans-serif;
    font-size: 17px; line-height: 1.15; color: var(--ink);
  }
  .contact li { display: flex; align-items: flex-start; gap: 9px; margin-bottom: 6px; }
  .contact .icon { width: 18px; height: 18px; flex: none; margin-top: 2px; }
  .contact .lines { display: flex; flex-direction: column; }
  .contact .web { font-size: 19px; }
  .swoosh { position: absolute; left: 0; bottom: 0; width: 520px; height: 297px; }
</style>
</head>
<body>
<main class="canvas">
  <section class="card card-front" aria-label="Card front">
    <div class="front-mark">
      <span class="dot"></span>
      <span class="wordmark">LNI</span>
    </div>
  </section>

  <section class="card card-back" aria-label="Card back">
    <svg class="swoosh" viewBox="0 0 520 297" aria-hidden="true">
      <path d="M0 205 Q 30 262 150 297 L0 297 Z" fill="var(--muted-curve)"/>
      <path d="M0 222 Q 35 272 120 297 L0 297 Z" fill="var(--brand-blue)"/>
    </svg>

    <h1 class="company-name">Lanternway Networks, Inc.</h1>

    <div class="person">
      <p class="person-name">Aldo Wren</p>
      <p class="person-title">Account Manager</p>
    </div>

    <ul class="contact">
      <li>
        <svg class="icon" viewBox="0 0 20 20" aria-hidden="true">
          <path d="M2 6 Q10 1 18 6 L16 8 L13 7 L13 5 Q10 4 7 5 L7 7 L4 8 Z" fill="var(--deep-blue)"/>
          <rect x="4" y="9" width="12" height="9" rx="1.5" fill="var(--deep-blue)"/>
          <g fill="var(--card-light)">
            <rect x="6" y="11" width="2" height="1.6"/><rect x="9" y="11" width="2" height="1.6"/><rect x="12" y="11" width="2" height="1.6"/>
            <rect x="6" y="14" width="2" height="1.6"/><rect x="9" y="14" width="2" height="1.6"/><rect x="12" y="14" width="2" height="1.6"/>
          </g>
        </svg>
        <span class="lines"><span>555014782</span><span>555029631</span></span>
      </li>
      <li>
        <svg class="icon" viewBox="0 0 20 20" aria-hidden="true">
          <rect x="1" y="4" width="18" height="12" fill="var(--deep-blue)"/>
          <path d="M1.5 4.5 L10 11 L18.5 4.5" fill="none" stroke="var(--card-light)" stroke-width="1.4"/>
        </svg>
        <span>aldo.wren@lni-sample.co</span>
      </li>
      <li>
        <svg class="icon" viewBox="0 0 20 20" aria-hidden="true">
          <circle cx="10" cy="10" r="8" fill="var(--deep-blue)"/>
          <g fill="none" stroke="var(--card-light)" stroke-width="1">
            <ellipse cx="10" cy="10" rx="3.5" ry="8"/>
            <line x1="2" y1="10" x2="18" y2="10"/>
            <line x1="3.5" y1="6" x2="16.5" y2="6"/>
            <line x1="3.5" y1="14" x2="16.5" y2="14"/>
          </g>
        </svg>
        <span class="web">www.lni-sample.co</span>
      </li>
    </ul>
  </section>
</main>
</body>
</html>
```